Rising Stewards Scheme. Brochure to Inform Target Audience.

Rising Steward Scheme:

4 Page Brochure
Aimed at Parents and Children (Age 11-16)
Programme Overview
Specific Focus on Copperleaf Award with Learning Objectives and Enabling Objectives from Content Document
Contact Area Needed
How to Book - Online through the Website
Should encourage people to want to join it or sign up

you can use stock rugby images if needed

Target Market(s)

children between ages 11-16 and parents, gatekeepers (schools, rugby clubs)

Industry/Entity Type

Education

Font styles to use
Serif
Sans Serif

Requirements
Must have
• the programme content, each award continent and Copperleaf Award learning objectives
• Colours should match existing work that has been created
• Get in touch: www.harvestmark-rss.com
• maren@harvestmark-rss.com
Nice to have
• graphics of kids playing rugby if possible from stock images

```html
<!DOCTYPE html>
<html lang="en">
<head>
<meta charset="utf-8">
<title>Rising Stewards Scheme – Brochure</title>
<link href="https://fonts.googleapis.com/css2?family=Ubuntu:wght@300;400;500;700&family=Open+Sans:wght@400;600&family=Oswald:wght@500;600&display=swap" rel="stylesheet">
<style>
:root{
  --yellow:#fdc010;
  --charcoal:#2d2d2d;
  --ink:#0b0b0b;
  --white:#ffffff;
  --muted:#cfcfcf;
  --stage:#d6d6d6;
}
*{margin:0;padding:0;box-sizing:border-box}
html,body{width:800px;height:1200px;overflow:hidden}
body{background:var(--stage);position:relative;font-family:"Open Sans",sans-serif;color:var(--white)}
.spread{position:absolute;left:44px;width:714px;height:506px;overflow:hidden}
.spread--outer{top:64px}
.spread--inner{top:630px}
.page{position:absolute;top:0;height:506px;overflow:hidden}
.page--left{left:0;width:357px;background:var(--charcoal)}
.page--right{left:357px;width:357px;background:var(--ink)}
.spread--inner .page--right{background:#313131}
.abs{position:absolute}
.heading{font-family:"Ubuntu",sans-serif;font-weight:700;text-transform:uppercase;letter-spacing:.2px}
.heading .accent{color:var(--yellow)}
.rule{position:absolute;width:16px;height:3px;background:var(--yellow);border-radius:2px}
.copy{font-size:6.4px;line-height:1.5;color:var(--muted);text-align:justify}
.photo{position:absolute}
.medal{position:absolute;border-radius:50%;display:flex;align-items:center;justify-content:center;text-align:center;
  font-family:"Ubuntu",sans-serif;font-weight:700;text-transform:uppercase;color:#3a2a10;line-height:1.05;box-shadow:0 2px 6px rgba(0,0,0,.5)}
.medal--silver{background:radial-gradient(circle at 40% 35%,#ffffff,#c9c9c9 55%,#8e8e8e)}
.medal--gold{background:radial-gradient(circle at 40% 35%,#fff3a8,#f0c020 55%,#b8860b)}
.medal--copper{background:radial-gradient(circle at 40% 35%,#ffd0a0,#e58a3a 55%,#a4531c)}
.medal::before{content:"";position:absolute;inset:8%;border-radius:50%;border:1px solid rgba(255,255,255,.45)}
/* outer spread */
.overview-title{left:38px;top:42px;font-size:14px;font-weight:400}
.overview-title .accent{font-weight:700}
.contact{left:0;width:357px;text-align:center}
.contact-title{top:436px;font-family:"Ubuntu",sans-serif;font-weight:700;font-size:12px;color:var(--yellow)}
.contact-line{font-size:9.5px;color:var(--muted)}
.contact-line b{color:var(--yellow);font-weight:600}
.cover-line{font-family:"Ubuntu",sans-serif;text-transform:uppercase;left:47px}
.cover-1{top:50px;font-size:26px;font-weight:300}
.cover-2{top:80px;font-size:35px;font-weight:700;color:var(--yellow)}
.cover-3{top:113px;font-size:19px;font-weight:500}
.brand{left:222px;top:34px;width:120px;text-align:center}
.brand-name{font-family:"Ubuntu",sans-serif;font-weight:700;font-size:9px;color:var(--yellow);letter-spacing:.5px}
.brand-dot{width:34px;height:34px;border-radius:50%;border:2px solid var(--yellow);margin:0 auto 5px}
.scheme{left:205px;top:116px;width:150px;text-align:center;font-family:"Oswald",sans-serif;color:var(--yellow)}
.scheme-name{font-size:17px;font-weight:600;letter-spacing:.3px;line-height:1}
.scheme-sub{font-size:8px;letter-spacing:3px;font-weight:500;margin-top:3px;display:flex;align-items:center;gap:5px;justify-content:center}
.scheme-sub::before,.scheme-sub::after{content:"";height:1px;width:22px;background:var(--yellow)}
/* inner spread */
.award-title{left:34px;font-size:16px}
.award-copy{left:34px;width:198px;font-size:5.3px}
.award-band{position:absolute;left:320px;width:37px;height:40px;background:var(--yellow)}
.objectives-title{left:34px;top:174px;font-family:"Ubuntu",sans-serif;font-weight:700;font-size:11px;color:var(--yellow)}
.objectives{left:34px;top:192px;list-style:none;font-size:6.6px;font-weight:600}
.objectives li{height:13.8px;display:flex;gap:4px;align-items:center}
.objectives li::before{content:"";width:5px;height:3px;border-left:1.2px solid var(--yellow);border-bottom:1.2px solid var(--yellow);transform:rotate(-45deg) translateY(-1px)}
.mission-title{left:43px;top:44px;font-size:16px}
.mission-copy{left:43px;top:80px;width:280px;font-size:8px;line-height:1.45;color:var(--muted)}
.value{position:absolute;left:43px;width:118px}
.value-name{font-family:"Ubuntu",sans-serif;font-weight:700;font-size:8px;color:var(--yellow)}
.value-copy{font-size:5.5px;line-height:1.5;color:var(--muted);margin-top:2px}
.value-photo{position:absolute;left:185px;width:136px;height:80px;background:linear-gradient(135deg,#2f6b2a,#4f8a36 50%,#d7b63a)}
.value-frame{position:absolute;left:177px;width:134px;height:88px;border-left:1px solid var(--yellow);border-bottom:1px solid var(--yellow)}
.booking{position:absolute;left:0;top:431px;width:335px;height:69px;background:var(--yellow);color:var(--ink);padding:22px 0 0 43px}
.booking-title{font-family:"Ubuntu",sans-serif;font-weight:700;font-size:19px;text-transform:uppercase;line-height:1}
.booking-line{font-size:13px;margin-top:4px}
.booking-line b{font-weight:700}
.base-strip{position:absolute;left:0;top:500px;width:714px;height:6px;background:var(--yellow)}
</style>
</head>
<body>

<!-- Outer spread: overview + cover -->
<section class="spread spread--outer">
  <div class="page page--left">
    <h2 class="heading overview-title abs">Programme <span class="accent">Overview</span></h2>
    <span class="rule" style="left:38px;top:60px"></span>
    <p class="copy abs" style="left:38px;top:70px;width:270px">The Stewards have created a programme which enables each individual to maximise their learning potential so that you can be the best you can be. We provide a fun and healthy environment which is supported by highly motivated coaches which provide excellent individual care and attention. The programme is delivered over three Awards: Copperleaf, Silver and Gold.</p>

    <div class="photo" role="img" aria-label="Rugby team in black kit performing a pre-match ceremony on the pitch" style="left:0;top:136px;width:357px;height:250px;background:linear-gradient(180deg,#2d2d2d 0%,#1c1c1c 35%,#2a3a22 80%,#1e2a18 100%)"></div>

    <svg class="abs" style="left:0;top:330px" width="357" height="130" viewBox="0 0 357 130" aria-hidden="true">
      <path d="M0 70 C90 40 200 70 357 20 L357 45 C220 95 100 60 0 100 Z" fill="#fdc010"/>
      <path d="M0 100 C100 60 220 95 357 45 L357 130 L0 130 Z" fill="#262626"/>
      <path d="M0 60 C110 25 220 60 357 10" fill="none" stroke="#fdc010" stroke-width="0.8"/>
    </svg>

    <div class="medal medal--silver" style="left:38px;top:322px;width:80px;height:80px;font-size:10px">Silver<br>Award</div>
    <div class="medal medal--gold" style="left:138px;top:322px;width:80px;height:80px;font-size:10px">Gold<br>Award</div>
    <div class="medal medal--copper" style="left:238px;top:322px;width:80px;height:80px;font-size:8.5px">Copperleaf<br>Award</div>

    <h3 class="contact contact-title abs">GET IN TOUCH</h3>
    <span class="rule" style="left:171px;top:452px;width:14px"></span>
    <p class="contact contact-line abs" style="top:460px">&#9993; maren@harvestmark-rss.com</p>
    <p class="contact contact-line abs" style="top:478px">&#9711; www.<b>harvestmark-rss</b>.com</p>
  </div>

  <div class="page page--right">
    <div class="photo" role="img" aria-label="Rugby player in green kit running with the ball" style="left:0;top:150px;width:357px;height:320px;background:linear-gradient(160deg,#1a1a1a 0%,#1f4a2c 35%,#2f6a3a 60%,#6a7f3a 85%,#c9b23a 100%)"></div>
    <svg class="abs" style="left:0;top:150px" width="357" height="356" viewBox="0 0 357 356" aria-hidden="true">
      <path d="M0 60 C80 40 160 80 357 0 L357 20 C180 100 90 60 0 95 Z" fill="#fdc010"/>
      <path d="M0 50 C120 20 200 60 357 10" fill="none" stroke="#fdc010" stroke-width="0.8"/>
      <path d="M0 280 C100 240 240 300 357 250 L357 356 L0 356 Z" fill="#0b0b0b"/>
      <path d="M0 300 C110 250 230 300 357 240 L357 262 C240 320 100 270 0 320 Z" fill="#fdc010"/>
      <path d="M0 270 C120 230 240 280 357 230" fill="none" stroke="#ffffff" stroke-width="0.6" opacity=".7"/>
    </svg>

    <p class="cover-line cover-1 abs">Inspiring</p>
    <p class="cover-line cover-2 abs">The Next</p>
    <p class="cover-line cover-3 abs">Generation</p>
    <span class="rule" style="left:47px;top:134px;width:32px"></span>

    <div class="brand abs">
      <div class="brand-dot"></div>
      <p class="brand-name">HARVESTMARK</p>
    </div>
    <div class="scheme abs">
      <p class="scheme-name">RISING STEWARDS</p>
      <p class="scheme-sub">SCHEME</p>
    </div>

    <p class="contact contact-line abs" style="top:478px">&#9711; www.<b>harvestmark-rss</b>.com</p>
  </div>
</section>

<!-- Inner spread: awards + mission -->
<section class="spread spread--inner">
  <div class="page page--left">
    <h2 class="heading award-title abs" style="top:44px">Copperleaf <span class="accent">Award</span></h2>
    <span class="rule" style="left:34px;top:63px"></span>
    <p class="copy award-copy abs" style="top:77px">The Copperleaf Award is focused on the 'Team' and is aimed at Children between the ages of 11 and 13. During the Award you will improve your self-confidence and independence whilst having the opportunity to lead and inspire others. We will encourage your natural skills and help you identify any areas that you may wish to develop in the future. Each day we will build your skills through both physical and mental challenges both on and off the pitch. The Award is over delivered over 5 days. Days 1 and 2 are delivered at the Home of Rugby, Ashbridge and days 3 to 5 are delivered at Wexmoor Rovers.</p>
    <span class="award-band" style="top:91px"></span>
    <div class="medal medal--copper" style="left:251px;top:76px;width:70px;height:70px;font-size:7.5px">Copperleaf<br>Award</div>

    <h3 class="objectives-title abs">LEARNING OBJECTIVES</h3>
    <ul class="objectives abs">
      <li>Demonstrate the attributes required to be a successful leader</li>
      <li>Demonstrate effective communication</li>
      <li>Demonstrate effective followership</li>
      <li>Demonstrate the attributes required to be a Team Player</li>
      <li>Demonstrate an understanding of the Harvestmark Values</li>
    </ul>

    <h2 class="heading award-title abs" style="top:277px">Silver <span class="accent">Award</span></h2>
    <span class="rule" style="left:34px;top:296px"></span>
    <p class="copy award-copy abs" style="top:310px">On completion of the Copperleaf Award you are eligible to enrol on the Silver Award which is focused on the 'Individual'. This is aimed at 13 to 14 year olds and is again delivered over a 5 day period split between Ashbridge and Wexmoor Rovers. During this award we will be empowering you to discover your own strengths and weakness in order to find your most natural leadership style so that we build transferable skills for the future.</p>
    <span class="award-band" style="top:324px"></span>
    <div class="medal medal--silver" style="left:251px;top:309px;width:70px;height:70px;font-size:8px">Silver<br>Award</div>

    <h2 class="heading award-title abs" style="top:385px">Gold <span class="accent">Award</span></h2>
    <span class="rule" style="left:34px;top:404px"></span>
    <p class="copy award-copy abs" style="top:418px">This is a 5 day residential course for all those who have successfully completed the Copperleaf and Silver Award. Aimed at 14+, this is the culmination of the Harvestmark Rising Stewards Scheme. During this award leaders will be challenged with a variety of practical exercises and on field activities in order to develop a rounded steward leader. Individuals will learn how to tackle complex problems and plan missions whilst feeling confident that they can lead others. These skills will equip them for their future learning and workplace environments.</p>
    <span class="award-band" style="top:434px"></span>
    <div class="medal medal--gold" style="left:251px;top:419px;width:70px;height:70px;font-size:8px">Gold<br>Award</div>
  </div>

  <div class="page page--right">
    <h2 class="heading mission-title abs">Our <span class="accent">Mission</span></h2>
    <span class="rule" style="left:43px;top:63px"></span>
    <p class="mission-copy abs">To educate, inspire, mentor and transfer key leadership skills to the next generation</p>

    <h2 class="heading mission-title abs" style="top:127px">Our <span class="accent">Values</span></h2>
    <span class="rule" style="left:43px;top:146px"></span>

    <div class="value" style="top:167px"><p class="value-name">Leadership</p><p class="value-copy">For the team to be truly successful we believe in developing leadership at all levels.</p></div>
    <div class="value" style="top:220px"><p class="value-name">Courage</p><p class="value-copy">We put the needs of the team ahead of the needs of our own.</p></div>
    <div class="value" style="top:263px"><p class="value-name">Selfless Commitment</p><p class="value-copy">We have the physical and mental courage to possess confidence, bravery and resolution when faced with danger or fear.</p></div>
    <div class="value" style="top:324px"><p class="value-name">Resilience</p><p class="value-copy">Our strength of character to overcome adversity and bounce back.</p></div>
    <div class="value" style="top:368px"><p class="value-name">Respect</p><p class="value-copy">We respect those people who we train with and compete against. We believe in equal treatment and opportunity for all.</p></div>

    <span class="value-frame" style="top:122px"></span>
    <div class="value-photo" role="img" aria-label="Rugby players contesting a lineout" style="top:122px"></div>
    <span class="value-frame" style="top:220px"></span>
    <div class="value-photo" role="img" aria-label="Rugby players in a tackle on the ground" style="top:220px;background:linear-gradient(135deg,#8a2a2a,#3f6b2e 55%,#2a5a8a)"></div>
    <span class="value-frame" style="top:319px"></span>
    <div class="value-photo" role="img" aria-label="Rugby players in yellow kit celebrating in front of a crowd" style="top:319px;background:linear-gradient(135deg,#5a3a2a,#c9a43a 55%,#3a5a2a)"></div>

    <div class="booking">
      <p class="booking-title">How to Book?</p>
      <p class="booking-line">Log in to <b>www.harvestmark-rss.com</b> &#8599;</p>
    </div>
  </div>
  <span class="base-strip"></span>
</section>

</body>
</html>
```